Herausgeber suchen Design
Zielgruppe
Wir sind Herausgeber einer Festschrift für unseren Doktor-/Habilvater, Prof. Dr. Wallmerk, und suchen ein hochwertiges Design für die Einladungskarten zu einem Symposium, im Rahmen dessen die Festschrift übergeben wird; Zielgruppe sind die Autoren der Festschrift, Alumnis und Weggefährten von Herrn Wallmerk
Aufgabenstellung
- Maße: 210 mm x 105 mm
- Einladungskarte: geklappt; Frontseite, 2 Innenseiten, Rückseite
- Zum Text siehe Datei 'Text Einladungskarte'
- Design eher traditionell/konservativ, da es sich um einen wissenschaftlichen Hintergrund handelt (Symposium, Übergabe Festschrift)
- Die Farben sollen mit dem Cover der Festschrift korrespondieren (vgl. Datei 'Templates_Research_Tessner', dort das erste Cover (TKM_PV_Q04)

```html
<!DOCTYPE html>
<html lang="de">
<head>
<meta charset="utf-8">
<title>Einladung Symposium – Festschrift Prof. Dr. Wallmerk</title>
<link href="https://fonts.googleapis.com/css2?family=Fira+Sans+Condensed:wght@300;400;600;700&display=swap" rel="stylesheet">
<style>
  :root {
    --bg: #e3e4e8;
    --blue: #1b6dbd;
    --navy: #2e3963;
    --navy-mid: #666889;
    --mist: #c9c9d6;
    --paper: #eeeef1;
    --white: #ffffff;
    --ink: #2c3460;
  }
  * { margin: 0; padding: 0; box-sizing: border-box; }
  html, body { width: 1200px; height: 960px; overflow: hidden; }
  body {
    background: var(--bg);
    font-family: "Fira Sans Condensed", "Arial Narrow", sans-serif;
    position: relative;
  }
  .card {
    position: absolute;
    left: 180px; top: 60px;
    width: 840px; height: 840px;
    box-shadow: 0 6px 24px rgba(20, 30, 60, .18);
  }
  .panel { position: absolute; left: 0; width: 840px; height: 420px; overflow: hidden; }
  .panel--upper { top: 0; background: var(--navy); }
  .panel--lower {
    top: 420px;
    background: linear-gradient(to bottom, var(--navy) 0%, var(--navy-mid) 26%, var(--mist) 44%, var(--paper) 68%, #f3f3f5 100%);
  }
  .title-band { position: absolute; left: 0; top: 0; width: 840px; height: 200px; background: var(--blue); }
  .margin-rule { position: absolute; left: 40px; top: 38px; width: 1.5px; height: 382px; background: var(--white); opacity: .9; }

  .masthead {
    position: absolute; left: 70px; top: 50px;
    display: flex; align-items: flex-end; gap: 22px;
  }
  .title {
    font-size: 70px; font-weight: 400; color: var(--white); letter-spacing: .5px; line-height: 1;
    white-space: nowrap;
  }
  .subtitle {
    font-size: 24px; font-weight: 300; color: var(--white); line-height: 1.2;
    white-space: nowrap; padding-bottom: 4px;
  }
  .event-date {
    position: absolute; left: 230px; top: 232px;
    font-size: 32px; font-weight: 300; color: var(--white);
  }
  .event-venue {
    position: absolute; left: 230px; top: 300px;
    font-size: 32px; font-weight: 300; color: var(--white); line-height: 1.1;
  }
  .event-address { display: block; font-size: 23px; margin-top: 4px; }

  .label {
    position: absolute; left: 70px;
    font-size: 20px; font-weight: 300; color: var(--white);
  }
  .label--editors { top: 24px; }
  .label--programme { top: 186px; font-size: 16px; font-weight: 700; color: var(--ink); }

  .editors {
    position: absolute; left: 230px; top: 24px;
    font-size: 20px; font-weight: 300; color: var(--white); line-height: 1.25;
  }
  .editors--second { left: 480px; }
  .editors__invite { margin-top: 12px; }

  .programme {
    position: absolute; left: 230px; top: 186px;
    list-style: none; font-size: 15px; color: var(--ink); line-height: 1.2;
  }
  .programme li { padding-left: 14px; position: relative; }
  .programme li::before { content: "•"; position: absolute; left: 0; }
  .programme .speaker { display: block; }

  .closing {
    position: absolute; left: 230px; top: 340px;
    font-size: 15px; color: var(--ink);
  }
  .rsvp-bar {
    position: absolute; left: 230px; right: 0; top: 368px; height: 34px;
    background: var(--navy); color: var(--white);
    font-size: 14px; font-weight: 600;
    display: flex; align-items: center; padding-left: 14px;
  }
</style>
</head>
<body>
  <main class="card">
    <section class="panel panel--upper">
      <div class="title-band"></div>
      <div class="margin-rule"></div>
      <div class="masthead">
        <h1 class="title">Symposium</h1>
        <p class="subtitle">anlässlich der Übergabe der Festschrift<br>an Prof. Dr. Hans-Joachim Wallmerk</p>
      </div>
      <p class="event-date">am 29. Juni 2018 um 16.00 Uhr</p>
      <p class="event-venue">im Gästehaus der Universität Nordstadt
        <span class="event-address">Lindenallee 12, 20100 Nordstadt</span></p>
    </section>

    <section class="panel panel--lower">
      <p class="label label--editors">Die Herausgeber</p>
      <div class="editors">
        <p>Prof. Dr. Jonas Kerber</p>
        <p>Prof. Dr. Martin L. Brandt</p>
        <p>Dr. Tobias Reimers</p>
        <p class="editors__invite">laden herzlich ein</p>
      </div>
      <div class="editors editors--second">
        <p>Prof. Dr. Felix Hartung</p>
        <p>StB PD Dr. Lorenz Ebbing</p>
      </div>

      <p class="label label--programme">Ablauf</p>
      <ul class="programme">
        <li>Begrüßung und Vorstellung der Festschrift<span class="speaker">Prof. Dr. Jonas Kerber</span></li>
        <li>„Fortentwicklung des Corporate Governance Reportings“<span class="speaker">Prof. Dr. Daniel R. Hofer, LL.M. (London)</span></li>
        <li>Diskussion</li>
        <li>„Neuere Entwicklungen im Rahmen der risikoorientierten Abschlussprüfung“<span class="speaker">Prof. Dr. Simon K. Wendt</span></li>
        <li>Diskussion</li>
      </ul>

      <p class="closing">Im Anschluss an das Symposium findet ein Umtrunk statt.</p>
      <p class="rsvp-bar">Um Antwort wird gebeten bis zum 18. Mai 2018 unter sekretariat@wiso.uni-nordstadt.de</p>
    </section>
  </main>
</body>
</html>
```